Addictives for Saltwater Products

Creating product label for some oem addictives for dosing into saltwater aquariums.

Labels will be printed on stickers then are stick on bottles. Bottles have round and rectangular shape.

General content as follows
Brand Logos - Brinelume
Product name - Tidewell Blend
Product sub name description 15 words
Product pictures

Product Description 200 words
Product Usage instruction 100 words

Reference design direction can google Vonto, Coralwick Deep, Pelvane, Shoalbright

The bottles will be black in colour..

Target Market(s)

Hobbist aka reefer

Industry/Entity Type

Saltwater aquarium

Requirements
Must have
• Related to saltwater
Nice to have
• Unique simple straightforward design.

```html
<!DOCTYPE html>
<html lang="en">
<head>
<meta charset="utf-8">
<title>Brinelume Tidewell Blend Label</title>
<link href="https://fonts.googleapis.com/css2?family=Archivo:ital,wght@0,400;1,400;1,800&family=Montserrat:wght@500&display=swap" rel="stylesheet">
<style>
  :root {
    --backdrop: #ebe3f1;
    --ocean-deep: #0b4f86;
    --ocean-mid: #1a9cc7;
    --lagoon: #22c6d2;
    --lagoon-light: #5cd3d8;
    --abyss: #123f86;
    --magenta: #c2266f;
    --magenta-dark: #a5145a;
    --white: #ffffff;
  }
  * { margin: 0; padding: 0; box-sizing: border-box; }
  html, body {
    width: 1200px; height: 1200px; overflow: hidden;
    background: var(--backdrop);
  }
  .label {
    position: absolute; left: 365px; top: 47px;
    width: 470px; height: 1105px; overflow: hidden;
    background: linear-gradient(180deg, var(--ocean-deep) 0%, var(--ocean-mid) 20%, var(--lagoon) 33%, var(--lagoon-light) 48%, #2a9fc0 62%, var(--abyss) 82%, var(--abyss) 100%);
    color: var(--white);
    font-family: "Archivo", Arial, sans-serif;
  }
  .brand-name {
    position: absolute; left: 0; width: 100%; top: 190px;
    text-align: center; font-size: 90px; font-weight: 800; font-style: italic;
    letter-spacing: -4px; line-height: 1;
  }
  .product-pill {
    position: absolute; left: 63px; top: 320px; width: 327px; height: 50px;
    border-radius: 25px; background: var(--magenta);
    font-family: "Montserrat", sans-serif; font-weight: 500; font-size: 30px;
    letter-spacing: 1px; text-align: center; line-height: 50px;
  }
  .tagline {
    position: absolute; left: 18px; right: 14px; top: 412px;
    font-size: 19px; font-style: italic; line-height: 30px; letter-spacing: -0.5px;
    color: #eef9fb;
  }
  .product-scene {
    position: absolute; left: 18px; top: 520px; width: 425px; height: 370px;
    border-radius: 48% 48% 44% 44% / 14% 14% 40% 40%;
    background: radial-gradient(ellipse at 55% 55%, #e089b6 0%, #3f8fb6 35%, #1a6aa0 65%, #0d3f74 100%);
  }
  .usage {
    position: absolute; left: 36px; right: 36px; top: 905px;
    font-size: 10.5px; line-height: 14px; letter-spacing: -0.5px;
  }
  .footer-band {
    position: absolute; left: 0; bottom: 0; width: 470px; height: 150px;
  }
  .footer-text {
    position: absolute; bottom: 30px; font-size: 16px; letter-spacing: -0.6px;
  }
  .footer-text.coverage { left: 35px; }
  .footer-text.weight { right: 50px; font-size: 18px; }
</style>
</head>
<body>
  <main class="label">
    <h1 class="brand-name">Brinelume</h1>
    <div class="product-pill">Tidewell Blend</div>
    <p class="tagline">Attacks a broad range of disease causing organisms: Bacterial, fungal, viral, and parasites (ick)</p>
    <div class="product-scene" role="img" aria-label="Illustration of a round reef aquarium bowl with coral, rocks and tropical fish"></div>
    <p class="usage">USAGE INSTRUCTIONS: Lorem ipsum dolor sit amet, consectetuer adipiscing elit, sed diam nonummy nibh euismod tincidunt ut laoreet dolore magna aliquam erat volutpat. Ut wisi enim ad minim veniam, quis nostrud exerci tation ullamcorper suscipit lobortis nisl</p>
    <svg class="footer-band" viewBox="0 0 470 150" aria-hidden="true">
      <path d="M0 28 Q235 78 470 22 L470 150 L0 150 Z" fill="var(--magenta)"/>
      <path d="M0 14 Q235 66 470 8 L470 22 Q235 78 0 28 Z" fill="var(--magenta)" opacity="0.85"/>
      <path d="M0 24 Q235 74 470 18" fill="none" stroke="var(--white)" stroke-width="8"/>
      <rect x="0" y="110" width="470" height="40" fill="var(--magenta-dark)"/>
    </svg>
    <span class="footer-text coverage">Treats up to 12 gallons</span>
    <span class="footer-text weight">NET WT. 0.25 OZ</span>
  </main>
</body>
</html>
```